Cover and back of brochure

Our company sells all kind of filters. Now we are planning to create an image brochure for our company. This brochure should represent our high quality standard, our competence and the trust of the clients in our company.

In the attachment I added covers of other catalogs which we like. Furthermore I added nice pictures in the attachment which were downloaded from framequarry. In the first place we downloaded these pictures in a small size, so that several examples can be created. After we decide which picture looks best on the cover, we will buy it in a higher resolution.

More information you find in the added pdf document.

It Company

```html
<!DOCTYPE html>
<html lang="de">
<head>
<meta charset="utf-8">
<title>Filter Brandt – Rückseite</title>
<link href="https://fonts.googleapis.com/css2?family=Gilda+Display&display=swap" rel="stylesheet">
<style>
  :root {
    --paper: #ffffff;
    --brand-green: #1a9400;
    --ink-light: #ffffff;
  }
  * { margin: 0; padding: 0; box-sizing: border-box; }
  html, body {
    width: 1200px;
    height: 1000px;
    overflow: hidden;
    background: var(--paper);
  }
  .back-cover {
    position: absolute;
    left: 20px;
    top: 81px;
    width: 1160px;
    height: 820px;
    background: var(--brand-green);
    color: var(--ink-light);
    font-family: "Gilda Display", "Times New Roman", serif;
  }
  .values {
    position: absolute;
    left: 0;
    top: 122px;
    width: 1156px;
    text-align: center;
    list-style: none;
  }
  .values li {
    font-size: 36px;
    line-height: 48px;
    letter-spacing: 0.5px;
  }
  .values .separator {
    font-size: 24px;
    line-height: 66px;
    height: 66px;
  }
  .contact-block {
    position: absolute;
    top: 652px;
    height: 120px;
    padding-left: 34px;
    border-left: 1px solid var(--ink-light);
    font-size: 21px;
    line-height: 30px;
  }
  .contact-block.address { left: 36px; width: 542px; }
  .contact-block.channels {
    left: 578px;
    width: 548px;
    border-right: 1px solid var(--ink-light);
    padding-left: 35px;
  }
  .contact-block p { white-space: nowrap; }
</style>
</head>
<body>
  <section class="back-cover">
    <ul class="values">
      <li>KOMPETENT</li>
      <li class="separator">.</li>
      <li>HILFSBEREIT</li>
      <li class="separator">.</li>
      <li>FREUNDLICH</li>
    </ul>

    <address class="contact-block address" style="font-style:normal">
      <p>FILTER - BRANDT e.K.</p>
      <p>Inhaber Konrad Albers</p>
      <p>Lindauer Str. 14</p>
      <p>12305 Berlin</p>
    </address>

    <div class="contact-block channels">
      <p>Tel: 030 / 555 0142</p>
      <p>Fax: 030 / 555 0143</p>
      <p>E-Mail: info@filter-brandt.de</p>
      <p>Web: www.filter-brandt.de</p>
    </div>
  </section>
</body>
</html>
```